eBook Cover Design Project - Winter Lantern Vows

We need an ebook cover design for our new digital only title for Marigold Press.

Marigold Press is Romance. Marigold will own Romance in digital-first as Velvetine owns Romance in print and ebook.

We are looking for FUN, MODERN, PREMIUM designs. Please keep the look clean and edgy but have fun with it; be flirty - it's romance!!!

Target Market(s)

30-55 year old women.

Industry/Entity Type

Digital

Requirements
Must have
• Must work as a black and white image as well as a colour image.
- Must be easily viewed at thumbnail size.
- Title must always be larger than the author name. Both must appear on cover.
- Final file should be a JPEG supplied at 2240 pixels (H) X 1400 pixels (W).
- See attached document for story report.
- If using people on the cover refer to character traits in story report.
Should not have
• Offensive or pornographic content.
- Too many elements – keep it simple.

```html
<!DOCTYPE html>
<html lang="en">
<head>
<meta charset="utf-8">
<title>Winter Lantern Vows — ebook cover</title>
<link rel="stylesheet" href="https://fonts.googleapis.com/css2?family=Righteous&family=Didact+Gothic&display=swap">
<style>
  :root {
    --teal-deep: #5fa89b;
    --teal-light: #8fcabd;
    --paper: #f5ece3;
    --paper-shadow: #d9cfc4;
    --tape: rgba(225, 240, 236, 0.55);
    --title-coral: #d47c68;
    --author-ink: #2f2f2f;
  }
  html, body {
    margin: 0;
    padding: 0;
    overflow: hidden;
    background: #ffffff;
  }
  .cover {
    position: relative;
    width: 747px;
    height: 1200px;
    overflow: hidden;
    background: var(--teal-deep);
  }
  .backdrop {
    position: absolute;
    inset: 0;
    background: radial-gradient(ellipse at 50% 35%, var(--teal-light) 0%, var(--teal-deep) 75%);
  }
  .artwork {
    position: absolute;
    inset: 0;
    width: 747px;
    height: 1200px;
  }
  .title {
    position: absolute;
    top: 255px;
    left: 150px;
    width: 500px;
    margin: 0;
    font-family: "Righteous", sans-serif;
    font-weight: 400;
    font-size: 82px;
    line-height: 88px;
    color: var(--title-coral);
    text-align: center;
    transform: rotate(-3deg);
  }
  .title span { display: block; }
  .author {
    position: absolute;
    left: 0;
    right: 0;
    top: 1130px;
    margin: 0;
    font-family: "Didact Gothic", sans-serif;
    font-size: 40px;
    letter-spacing: 1px;
    color: var(--author-ink);
    text-align: center;
  }
</style>
</head>
<body>
<main class="cover">
  <div class="backdrop" role="img" aria-label="Teal background with a soft polka dot pattern"></div>

  <svg class="artwork" viewBox="0 0 747 1200" aria-hidden="true">
    <path class="paper-heart"
          d="M400,200 C360,110 230,70 160,140 C90,210 130,330 210,420 C290,510 370,560 430,615 C470,540 560,470 610,380 C660,290 650,170 560,120 C490,85 430,130 400,200 Z"
          fill="var(--paper)"/>
    <rect class="tape tape-top" x="470" y="90" width="160" height="80" fill="var(--tape)"
          transform="rotate(-32 550 130)"/>
    <rect class="tape tape-bottom" x="250" y="520" width="170" height="80" fill="var(--tape)"
          transform="rotate(4 335 560)"/>
    <path class="torn-strip-shadow"
          d="M0,1050 L30,1040 L55,1056 L90,1044 L120,1058 L160,1046 L200,1060 L240,1048 L280,1062 L320,1050 L360,1064 L400,1052 L440,1066 L480,1054 L520,1068 L560,1056 L600,1070 L640,1058 L680,1072 L720,1060 L747,1068 L747,1200 L0,1200 Z"
          fill="var(--paper-shadow)"/>
    <path class="torn-strip"
          d="M0,1060 L28,1050 L58,1066 L92,1054 L124,1068 L158,1056 L198,1070 L238,1058 L278,1072 L318,1060 L358,1074 L398,1062 L438,1076 L478,1064 L518,1078 L558,1066 L598,1080 L638,1068 L678,1082 L718,1070 L747,1078 L747,1200 L0,1200 Z"
          fill="var(--paper)"/>
  </svg>

  <h1 class="title"><span>Winter</span><span>Lantern</span><span>Vows</span></h1>
  <p class="author">Maren Talloway</p>
</main>
</body>
</html>
```